...

.

Hi Guys just to clarify.

All the images will be pulled straight from our website.

It will consist of 4 pages.
- Cover Page
- Light & Flag
- Flag Only
- Replacement Parts

The main work is just the layout and organisation of the item son the page. Along with an attractive/professional header and the like.

If you need any more help please let me know.

Website is www.brindlemast.com.au

Target Market(s)

- Mining Companies

- Off-Road 4x4 Companies

Requirements
Must have
• .
Nice to have
• .
Should not have
• .

```html
<!DOCTYPE html>
<html lang="en">
<head>
<meta charset="utf-8">
<title>Brindle Mast Australia – Catalogue of Products</title>
<link href="https://fonts.googleapis.com/css2?family=Oswald:wght@500;700&family=Roboto+Condensed:wght@400;700&display=swap" rel="stylesheet">
<style>
:root{
  --bg:#f4f3f1;
  --paper:#ffffff;
  --brown:#6e4326;
  --brown-light:#a07a5c;
  --red:#c8262c;
  --ink:#4a3a30;
  --muted:#8d8077;
  --sky:#c9d6dd;
  --earth:#b7835a;
  --steel:#9aa0a3;
}
*{box-sizing:border-box;margin:0;padding:0}
html,body{width:1200px;height:617px;overflow:hidden;background:var(--bg)}
body{font-family:"Roboto Condensed",Arial,sans-serif;color:var(--ink);position:relative}
.spread{position:absolute;top:96px;height:425px;display:flex;box-shadow:0 6px 18px rgba(0,0,0,.15)}
.spread--outer{left:30px}
.spread--inner{left:610px}
.page{width:280px;height:425px;background:var(--paper);position:relative;overflow:hidden;padding:18px 16px}
.page + .page{border-left:1px solid #e2ddd8}
.page-title{font-family:"Oswald",Impact,sans-serif;font-weight:700;color:var(--brown);font-size:22px;letter-spacing:.5px;text-transform:uppercase;line-height:1;position:relative;z-index:2}
.section-title{font-family:"Oswald",Impact,sans-serif;font-weight:500;color:var(--red);font-size:12px;text-transform:uppercase;letter-spacing:.5px;margin:10px 0 5px}
.section-title--center{text-align:center}
.copy{font-size:7.5px;line-height:1.35;color:var(--ink)}
.rule{height:4px;background:var(--brown-light);opacity:.5;margin-top:5px}

/* replacement parts */
.part-row{display:flex;gap:8px}
.part{flex:1;display:flex;gap:5px;align-items:flex-start}
.part-img{flex:none;border-radius:2px}
.part-code{font-weight:700;font-size:6.5px;color:var(--brown)}
.part-desc{font-size:6.5px;line-height:1.3}
.flag-icon{width:18px;height:13px;background:linear-gradient(135deg,var(--red) 45%,#fff 45%,#fff 55%,var(--red) 55%)}
.glory-icon{width:10px;height:16px;background:linear-gradient(var(--red),#e77)}
.base-icon{width:16px;height:38px;background:linear-gradient(90deg,#3f4a86,#7b86c4,#3f4a86);border-radius:3px}
.qd-icon{width:12px;height:22px;background:linear-gradient(90deg,#777,#ccc,#777)}

/* cover */
.cover-url{font-size:8px;color:var(--brown);font-weight:700;letter-spacing:.5px}
.cover-title{font-family:"Oswald",Impact,sans-serif;font-weight:700;color:var(--brown);font-size:27px;line-height:1;margin-top:8px;text-transform:uppercase}
.cover-tag{margin-top:12px;width:150px;height:26px;border:1px solid #ddd;background:#f7f7f7;color:#b9b2ad;font-size:9px;display:flex;align-items:center;justify-content:center}
.brand{margin-top:36px;display:flex;align-items:center;gap:8px}
.brand-mark{width:22px;height:22px;background:var(--brown)}
.brand-name{font-family:"Oswald",Impact,sans-serif;font-weight:700;color:var(--brown);font-size:22px;text-transform:uppercase}
.brand-sub{font-size:8px;font-weight:700;color:var(--brown);letter-spacing:1px;margin-top:3px;text-transform:uppercase}
.cover-photo{position:absolute;left:0;right:0;bottom:0;height:150px;background:linear-gradient(180deg,var(--sky) 0%,#dfe3dc 40%,var(--earth) 70%,#8c5f3c 100%)}

/* inner pages */
.photo-top{position:absolute;right:0;top:0;width:112px;height:70px;background:linear-gradient(180deg,var(--sky),#c8b69a 60%,var(--earth))}
.aerial{position:absolute;width:14px;height:210px;background:linear-gradient(180deg,var(--red) 0 22px,#333 22px 26px,var(--red) 26px 92%,#888 92%)}
.aerial--left{left:16px;top:120px}
.aerial--right{right:16px;top:120px}
.col-text{margin-left:40px}
.col-text--right{margin-left:0;margin-right:40px}
.base-set{display:flex;gap:6px;justify-content:center;margin-top:8px}
.base-set .base{width:14px;height:46px;background:linear-gradient(90deg,#666,#ddd,#666);border-radius:2px}
.flag-pair{display:inline-flex;gap:3px;vertical-align:middle;margin-right:4px}
.flag-pair span{width:12px;height:8px;background:var(--red)}
.flag-pair span + span{background:#f08ab4}
</style>
</head>
<body>

<section class="spread spread--outer">
  <article class="page page--parts">
    <h2 class="page-title">Replacement Parts</h2>
    <div class="rule"></div>

    <h3 class="section-title">Flags</h3>
    <div class="part-row">
      <div class="part"><div class="part-img flag-icon" role="img" aria-label="Red mesh flag"></div><div><p class="part-code">BMA PART # F100</p><p class="part-desc">Replacement Mesh Flag (300mm x 450mm)</p></div></div>
      <div class="part"><div class="part-img flag-icon" role="img" aria-label="Red and white mesh flag"></div><div><p class="part-code">BMA PART # F101</p><p class="part-desc">Replacement Mesh Flag (300mm x 450mm)</p></div></div>
    </div>

    <h3 class="section-title">Glories</h3>
    <div class="part-row">
      <div class="part"><div class="part-img glory-icon" role="img" aria-label="Red LED glory light"></div><div><p class="part-code">BMA PART # G200</p><p class="part-desc">Replacement LED Glory (Red)</p></div></div>
      <div class="part"><div class="part-img glory-icon" role="img" aria-label="Red incandescent glory light"></div><div><p class="part-code">BMA PART # G201</p><p class="part-desc">Replacement Incandescent Glory (Red)</p></div></div>
    </div>

    <h3 class="section-title">Spring Bases</h3>
    <div class="part-row">
      <div class="part"><div class="part-img base-icon" role="img" aria-label="Blue spring base"></div><div><p class="part-code">BMA PART # SB300</p><p class="part-desc">Spring Base 25mm x 100mm Suitable for Aerials 1.8m to 4.5m</p></div></div>
      <div class="part"><div class="part-img base-icon" role="img" aria-label="Blue heavy spring base"></div><div><p class="part-code">BMA PART # SB301</p><p class="part-desc">Spring Base 32mm x 120mm Suitable for Aerials 3.0m to 6.0m</p></div></div>
    </div>

    <h3 class="section-title">Quick Disconnections</h3>
    <div class="part-row">
      <div class="part"><div class="part-img qd-icon" role="img" aria-label="Quick disconnect set"></div><div><p class="part-code">BMA PART # QD400</p><p class="part-desc">Complete Quick Disconnect Set</p></div></div>
      <div class="part"><div class="part-img qd-icon" role="img" aria-label="Male insert"></div><div><p class="part-code">BMA PART # QD401</p><p class="part-desc">Male Insert</p></div></div>
      <div class="part"><div class="part-img qd-icon" role="img" aria-label="Female socket"></div><div><p class="part-code">BMA PART # QD402</p><p class="part-desc">Female Socket</p></div></div>
    </div>
  </article>

  <article class="page page--cover">
    <p class="cover-url">www.brindlemast.com.au</p>
    <h1 class="cover-title">Catalogue of Products</h1>
    <p class="cover-tag">Built for the bush</p>
    <div class="brand"><span class="brand-mark"></span><span class="brand-name">Brindlemast</span></div>
    <p class="brand-sub">Brindle Mast Australia</p>
    <div class="cover-photo" role="img" aria-label="Photo of utility vehicles with safety aerials in the outback"></div>
  </article>
</section>

<section class="spread spread--inner">
  <article class="page page--light-flag">
    <h2 class="page-title">Light &amp; Flag</h2>
    <div class="photo-top" role="img" aria-label="Photo of a white ute fitted with a safety aerial"></div>
    <div class="aerial aerial--left" role="img" aria-label="Safety aerial with red flag and light"></div>
    <div class="col-text" style="margin-top:36px">
      <h3 class="section-title">Lighting</h3>
      <p class="copy">Your choice of LED or incandescent glory lights, fitted to the top of the aerial. LED glories draw far less power.</p>
      <h3 class="section-title">Flags</h3>
      <p class="copy"><span class="flag-pair"><span></span><span></span></span>Choose your flag colour and size. Our standard mesh flag is high visibility and made to last in harsh conditions.</p>
      <h3 class="section-title section-title--center">Rod and Tubing</h3>
      <p class="copy">Our fibreglass rod is flexible and strong, sleeved in PVC tubing. Lengths run from 1.8m to 4.5m to suit your site rules.</p>
      <h3 class="section-title section-title--center">Bases</h3>
      <p class="copy">Your choice of our standard bolt-on base or a spring base. Spring bases let the aerial flex on impact and return upright. Quick disconnect fittings allow the aerial to be removed in seconds.</p>
      <div class="base-set" role="img" aria-label="Range of aerial bases"><span class="base"></span><span class="base"></span><span class="base"></span><span class="base"></span></div>
    </div>
  </article>

  <article class="page page--flag-only">
    <h2 class="page-title" style="text-align:right">Flag Only</h2>
    <div class="aerial aerial--right" role="img" aria-label="Safety aerial with red flag"></div>
    <div class="col-text--right">
      <h3 class="section-title section-title--center">Flags</h3>
      <p class="copy">Choose your flag colour and size from our standard range. All flags are UV stabilised mesh.</p>
      <h3 class="section-title">Splits, PVC Tubing &amp; Rod</h3>
      <p class="copy">Splitting the rod makes transport and storage easy. Each split joins with a threaded brass ferrule and is sleeved in PVC tubing for protection. Rods come in a range of lengths to suit most vehicles and sites.</p>
      <h3 class="section-title section-title--center">Bases</h3>
      <p class="copy">Your choice of our standard bolt-on base or a spring base. Quick disconnect fittings are also available. Small spring bases suit light vehicles, larger spring bases suit mine site trucks.</p>
      <div class="base-set" role="img" aria-label="Range of aerial bases"><span class="base"></span><span class="base"></span><span class="base"></span><span class="base"></span></div>
    </div>
  </article>
</section>

</body>
</html>
```